QUOTE Graphics for Summer Challenge

I would like to put these quotes over one of the pictures attached; For Instagram, use new size: 4:5 (1080 x 1350 pixels). One Quote per picture, and I want the quote to be bold or easy to read as well. I provided a few reference graphics that I really like as examples below.
All of the pictures are attached; you can pick any photo and add one quote to it; but no stock photography
All the quotes are in the attached WORD document

```html
<!DOCTYPE html>
<html lang="en">
<head>
<meta charset="utf-8">
<title>Sunshine Season Slimdown</title>
<link href="https://fonts.googleapis.com/css2?family=Montserrat:wght@300;700;800&family=Bebas+Neue&display=swap" rel="stylesheet">
<style>
  :root {
    --page: #ffffff;
    --ink-light: #ffffff;
    --navy: #0e3d55;
    --pink: #ec6180;
    --panel: rgba(30, 26, 20, 0.55);
    --grass: #5f8a3a;
    --foliage: #3f6a2c;
    --crochet: #6b4326;
  }
  * { margin: 0; padding: 0; box-sizing: border-box; }
  html, body {
    width: 1109px; height: 1200px; overflow: hidden;
    background: var(--page);
    font-family: "Montserrat", Arial, sans-serif;
  }
  .poster {
    position: absolute; left: 117px; top: 72px;
    width: 810px; height: 1011px; overflow: hidden;
  }
  .poster-photo {
    position: absolute; inset: 0;
    background:
      radial-gradient(ellipse 220px 520px at 52% 62%, var(--crochet) 0%, rgba(107,67,38,0.85) 55%, rgba(107,67,38,0) 100%),
      radial-gradient(ellipse 140px 180px at 52% 18%, #3a2418 0%, rgba(58,36,24,0) 100%),
      linear-gradient(90deg, var(--foliage) 0%, #6f8f48 30%, rgba(120,110,90,0.6) 70%, #4d5a58 100%),
      linear-gradient(180deg, #5a7a3a 0%, var(--grass) 70%, #6b9a40 100%);
  }
  .text-panel {
    position: absolute; left: 74px; top: 228px;
    width: 662px; height: 685px;
    background: var(--panel);
  }
  .headline-lead {
    position: absolute; left: 0; right: 0; top: 258px;
    text-align: center; color: var(--ink-light);
    font-weight: 800; font-size: 56px; line-height: 47px;
    letter-spacing: -0.5px;
  }
  .headline-punch {
    position: absolute; left: 0; right: 0; top: 418px;
    text-align: center; color: var(--ink-light);
    font-family: "Bebas Neue", "Oswald", sans-serif;
    font-size: 172px; line-height: 140px; letter-spacing: 1px;
  }
  .detox-banner {
    position: absolute; left: 96px; top: 581px;
    width: 617px; height: 72px; background: var(--ink-light);
    display: flex; align-items: center; justify-content: center;
    font-weight: 800; font-size: 38px; color: var(--navy);
    letter-spacing: 0.3px; white-space: nowrap;
  }
  .detox-banner .accent { color: var(--pink); margin: 0 11px; }
  .cta-comment {
    position: absolute; left: 0; right: 0; top: 678px;
    text-align: center; color: var(--ink-light);
    font-weight: 300; font-size: 55px; line-height: 55px; letter-spacing: 1px;
  }
  .cta-keyword-rule {
    position: absolute; top: 768px; height: 2px; background: var(--ink-light);
  }
  .cta-keyword-rule.left { left: 168px; width: 53px; }
  .cta-keyword-rule.right { left: 589px; width: 51px; }
  .cta-keyword {
    position: absolute; left: 221px; top: 734px;
    width: 368px; height: 68px;
    border: 2px solid var(--ink-light);
    display: flex; align-items: center; justify-content: center;
    color: var(--pink); font-weight: 800; font-size: 66px; letter-spacing: 1px;
  }
  .cta-join {
    position: absolute; left: 0; right: 0; top: 816px;
    text-align: center; color: var(--ink-light);
    font-weight: 800; font-size: 39px; line-height: 39px; letter-spacing: 0.5px;
  }
  .handle {
    position: absolute; left: 0; right: 0; top: 932px;
    text-align: center; color: var(--ink-light);
    font-weight: 700; font-size: 16px;
  }
</style>
</head>
<body>
  <main class="poster">
    <div class="poster-photo" role="img" aria-label="Photo of a woman in a brown crochet outfit posing on a sunny lawn in front of a modern house"></div>
    <div class="text-panel"></div>
    <h1 class="headline-lead">FEELING<br>BLOATED,<br>SLUGGISH, AND</h1>
    <p class="headline-punch">TOO BIG?</p>
    <p class="detox-banner">YOUR<span class="accent">DETOX</span>STARTS NOW</p>
    <p class="cta-comment">COMMENT</p>
    <span class="cta-keyword-rule left"></span>
    <span class="cta-keyword-rule right"></span>
    <p class="cta-keyword">SUMMER</p>
    <p class="cta-join">TO JOIN THE SUNSHINE<br>SEASON SLIMDOWN</p>
    <p class="handle">@MayaRiversOnline</p>
  </main>
</body>
</html>
```